依頼詳細
・当社で建築した物件とイメージキャラクターをデザインに盛り込んだ提案をお願いします。(添付ファイル有)
・封筒の色は白で考えています。
・封筒サイズ:角2、角0(角2と同じデザイン)、長3(縦向き)
記載項目
・会社ロゴ ・会社マーク ※添付ファイル有
〒245-0623
神奈川県横浜市戸塚区下柏尾町517-4 リベルタ北園3F
TEL 045-770-2914(代表)
045-770-2957(工事部)
045-770-2986(不動産部)
FAX 045-770-2938
www.hinorisa-corp.com
E-mail info@hinorisa-corp.com
・当社で建築した物件(添付ファイル写真)のいずれかを背景等に使って下さい。
・イメージキャラクター ヒノリくん(添付ファイル有)
希望イメージ
• +5 0 +5
• シンプル
複雑
• 単色
カラフル
• 暗い
明るい
• 日常
高級
• 遊び心
厳粛
• 未来的
伝統的
• 女性的
男性的
希望する色
緑系、黄・オレンジ系、物件写真はモノクロやセピア調に加工して頂いてもかまいません。
納品ファイル
• 高解像度JPG (.jpg)
補足説明
当社の名刺も添付します。
3段目、4段目のような雰囲気をイメージして頂くといいかと思います。
依頼公開後の追記内容
■ 選んだ理由

色使いや配置が細部にわたりバランス良く、綺麗にまとまっていました。
重要な書類の送付にも問題なく、また社員投票でも一番人気だったので選ばせて頂きました。

■ 提案者全員のお礼・コメント

ランサーの皆さま、この度は当社の会社封筒デザインにたくさんの素敵なご提案を頂きましてありがとうございます。

皆さまの作品のコメントを拝見すると、どれも「なるほど!」と思うものばかりで、一点を選ぶのに大変苦労しました。

また何かご縁がありました際にはよろしくお願い致します。

```html
<!DOCTYPE html>
<html lang="ja">
<head>
<meta charset="utf-8">
<title>ヒノリサコーポレーション 長3封筒</title>
<link href="https://fonts.googleapis.com/css2?family=Noto+Sans+JP:wght@400;700;900&family=Tinos&display=swap" rel="stylesheet">
<style>
  :root {
    --paper: #ffffff;
    --edge: #e4e4e4;
    --leaf-dark: #2f5d1c;
    --leaf: #7bb23a;
    --leaf-light: #b9d77a;
    --straw: #e7c94a;
    --straw-deep: #c89a2e;
    --ink: #333333;
    --accent-red: #c8322a;
  }
  html, body {
    margin: 0;
    padding: 0;
    width: 1200px;
    height: 2348px;
    overflow: hidden;
    background: var(--paper);
  }
  .envelope {
    position: relative;
    width: 1200px;
    height: 2348px;
    box-sizing: border-box;
    border: 3px solid var(--edge);
    background: var(--paper);
    font-family: "Noto Sans JP", sans-serif;
    color: var(--ink);
  }
  .photo-band {
    position: absolute;
    left: 0;
    top: 1432px;
    width: 100%;
    height: 556px;
    overflow: hidden;
  }
  .photo-band__building {
    position: absolute;
    inset: 0;
    background: linear-gradient(120deg, rgba(200,154,46,0.85) 0%, rgba(231,201,74,0.9) 28%, rgba(185,215,122,0.85) 55%, rgba(123,178,58,0.9) 80%, rgba(47,93,28,0.85) 100%);
  }
  .photo-band__glow {
    position: absolute;
    inset: 0;
    background: linear-gradient(180deg, rgba(255,255,240,0.35) 0%, rgba(255,255,255,0) 45%, rgba(255,255,220,0.25) 100%);
  }
  .slogan {
    position: absolute;
    left: 448px;
    top: 1480px;
    width: 450px;
    margin: 0;
    font-family: "Tinos", serif;
    font-weight: 400;
    font-size: 80px;
    line-height: 134px;
    color: var(--leaf-dark);
    white-space: nowrap;
  }
  .slogan span { display: block; }
  .web {
    position: absolute;
    left: 592px;
    top: 1914px;
    font-size: 26px;
    line-height: 36px;
    color: var(--leaf-dark);
    white-space: nowrap;
  }
  .mascot {
    position: absolute;
    left: 920px;
    top: 1580px;
    width: 244px;
    height: 384px;
    border-radius: 40px;
    background: linear-gradient(180deg, #f3e27a 0%, #e9a23a 100%);
  }
  .brand {
    position: absolute;
    left: 80px;
    top: 2030px;
    display: flex;
    align-items: center;
    gap: 28px;
  }
  .brand__square {
    width: 160px;
    height: 60px;
    background: var(--accent-red);
  }
  .brand__name {
    font-size: 38px;
    line-height: 60px;
    font-weight: 700;
    color: #111111;
    white-space: nowrap;
  }
  .contact {
    position: absolute;
    left: 80px;
    top: 2126px;
    margin: 0;
    font-size: 23px;
    line-height: 40px;
    color: var(--ink);
  }
  .contact p { margin: 0; white-space: nowrap; }
  .contact .tel { color: var(--accent-red); font-weight: 700; }
  .contact .tel .sub { color: var(--ink); font-weight: 400; }
</style>
</head>
<body>
<div class="envelope">
  <div class="photo-band">
    <div class="photo-band__building" role="img" aria-label="当社で建築した住宅の外観と室内の写真を黄色と緑のトーンで重ねた背景"></div>
    <div class="photo-band__glow"></div>
  </div>
  <h1 class="slogan"><span>GOOD</span><span>HOUSE</span><span>PRODUCTS</span></h1>
  <div class="web">www.hinorisa-corp.com</div>
  <div class="mascot" role="img" aria-label="イメージキャラクター ヒノリくん"></div>

  <div class="brand">
    <div class="brand__square"></div>
    <div class="brand__name">株式会社 ヒノリサコーポレーション</div>
  </div>

  <div class="contact">
    <p>〒245-0623　神奈川県横浜市戸塚区下柏尾町517-4　リベルタ北園3F</p>
    <p class="tel">TEL. 045-770-2914(代表) <span class="sub">045-770-2957(工事部)　045-770-2986(不動産部)</span></p>
    <p>FAX. 045-770-2938</p>
    <p>E-mail : info@hinorisa-corp.com</p>
  </div>
</div>
</body>
</html>
```